Not another boring Business Card Design Project

This is not another boring Business Card Design Project.

We are looking for the weirdest, wackiest most boundary pushing designs that you can come up with.

If you believe that design can be fun, energetic, crazy, unpredictable, beautiful and eye-catching then read on… this project is for you.

We are Tolvin Presk and we print plastic cards.

We are running a Plastic Card Design Competition.

And we need a plastic card to advertise the competition to graphic designers just like you.

The design needs to make your average designers’ jaws drop and their eyes pop out.

You can do what you wish with the card design, so long as it stands out.

We like these designs, designs that stretch the boundaries and become something beyond just another business card:

http://quorvamedia.net/wp-content/uploads/2009/03/b48.jpg
Designer - http://www.pelvanworks.com/

http://quorvamedia.net/wp-content/uploads/2009/03/b41.jpg
Designer - http://renolbrakstad.com/

http://images.plinthhive.com/designs/44195_732292_37774_thumbnail.jpg
Designer- Zentro Media at Plinth Hive

http://images.plinthhive.com/designs/44195_717529_37774_thumbnail.jpg
Designer - Zentro Media at Plinth Hive

http://quorvamedia.net/wp-content/uploads/2009/03/b11.jpg
Designer - http://www.wk7studio.com/

http://quorvamedia.net/wp-content/uploads/2009/03/b16.jpg
Designer - http://www.pebbletumbler.com/

Reason: A number of designers have said they want to submit designs and haven't yet done so, we want to give them time.

Reason: We've extended the deadline by 4 days for those who want to submit their designs over the weekend and give ourselves time to judge them

Plastic

• The design needs to contain this link: lnk.example/QzRpLk and any other detail that will encourage competition entry. The design will be printed on plastic.
• No borders (when plastic cards are punched to shape and size there is movement of 1 - 2mm, borders highlight this movement).

Keep text 3mm away from edges of the cards.

Please don't create designs to be produced on clear/transparent plastic.

```html
<!DOCTYPE html>
<html lang="en">
<head>
<meta charset="utf-8">
<title>Plastic Card Design Competition</title>
<link rel="stylesheet" href="https://fonts.googleapis.com/css2?family=Roboto+Condensed:wght@400;700&family=Noto+Serif:wght@700&family=Kaushan+Script&family=Fredoka:wght@600&display=swap">
<style>
  :root {
    --red-bright: #ff2626;
    --red-deep: #b3141a;
    --question-red: #9e1a1d;
    --panel-navy: #1b3878;
    --panel-blue: #2a5cf7;
    --lime: #7cf23a;
    --cyan: #3fe6ff;
    --gold: #ffd21c;
    --amber: #f3a10d;
    --white: #ffffff;
    --ink: #111111;
  }
  html, body {
    margin: 0;
    padding: 0;
    overflow: hidden;
    background: #e9e9e9;
  }
  .card {
    position: relative;
    width: 1200px;
    height: 777px;
    overflow: hidden;
    background: linear-gradient(170deg, var(--red-bright) 0%, #e81d22 40%, var(--red-deep) 100%);
  }
  .splatter {
    position: absolute;
    left: 460px;
    top: 50px;
    width: 740px;
    height: 727px;
    background:
      radial-gradient(ellipse 45% 40% at 78% 72%, rgba(63, 230, 255, 0.55), rgba(63, 230, 255, 0) 70%),
      radial-gradient(ellipse 50% 55% at 30% 58%, rgba(124, 242, 58, 0.55), rgba(124, 242, 58, 0) 72%);
  }
  .wall-panel {
    position: absolute;
    left: 131px;
    top: 0;
    width: 328px;
    height: 777px;
    background: linear-gradient(90deg, var(--panel-navy) 0%, #2247b8 55%, var(--panel-blue) 100%);
  }
  .headline {
    position: absolute;
    left: 150px;
    top: 62px;
    margin: 0;
    font-family: "Roboto Condensed", "Arial Narrow", sans-serif;
    font-weight: 700;
    font-size: 104px;
    line-height: 92px;
    color: var(--lime);
    text-transform: uppercase;
    transform: rotate(-9deg);
    transform-origin: left top;
    letter-spacing: 1px;
  }
  .headline span {
    display: block;
  }
  .question-mark {
    position: absolute;
    left: 870px;
    top: 110px;
    font-family: "Noto Serif", Georgia, serif;
    font-weight: 700;
    font-size: 610px;
    line-height: 1;
    color: var(--question-red);
  }
  .or-win {
    position: absolute;
    left: 468px;
    top: 400px;
    margin: 0;
    font-family: "Fredoka", "Trebuchet MS", sans-serif;
    font-weight: 600;
    font-size: 128px;
    line-height: 1;
    color: var(--gold);
    background: linear-gradient(180deg, #fff06a 0%, var(--gold) 45%, var(--amber) 100%);
    -webkit-background-clip: text;
    background-clip: text;
    -webkit-text-fill-color: transparent;
    transform: skewX(-14deg);
    filter: drop-shadow(5px 6px 0 var(--ink));
    letter-spacing: 2px;
  }
  .info-label {
    position: absolute;
    left: 131px;
    top: 648px;
    font-family: "Roboto Condensed", "Arial Narrow", sans-serif;
    font-weight: 700;
    font-size: 34px;
    line-height: 1;
    color: var(--cyan);
  }
  .visit {
    position: absolute;
    left: 22px;
    top: 682px;
    font-family: "Kaushan Script", cursive;
    font-size: 52px;
    line-height: 1;
    color: var(--lime);
    text-shadow: 3px 3px 0 var(--ink), -1px -1px 0 var(--ink), 1px -1px 0 var(--ink), -1px 1px 0 var(--ink);
  }
  .entry-link {
    position: absolute;
    left: 131px;
    top: 684px;
    font-family: "Roboto Condensed", "Arial Narrow", sans-serif;
    font-weight: 400;
    font-size: 50px;
    line-height: 1;
    color: var(--white);
  }
</style>
</head>
<body>
  <main class="card">
    <div class="splatter" role="img" aria-label="Lime green and cyan paint splatter spraying across the red background"></div>
    <div class="wall-panel"></div>
    <h1 class="headline">
      <span>Stay</span>
      <span>Within</span>
      <span>These</span>
      <span>Walls</span>
    </h1>
    <div class="question-mark" aria-hidden="true">?</div>
    <p class="or-win">or win</p>
    <div class="info-label">For more information</div>
    <div class="visit">visit</div>
    <div class="entry-link">lnk.example/QzRpLk</div>
  </main>
</body>
</html>
```